Webdesign für Anbieter von Erotik-Geschichten
Zielgruppe
Wir sind ein Anbieter von Erotik-Geschichten. Die Marke heisst Lunvo Erotica. Das Erlebnis für die Kunden soll hochwertig und persönlich wirken. Daher in keiner Art und Weise schmuddelig. Die Zielgruppe sind Frauen ab ca. 20-40. Die Geschichten werden frei lesbar sein, d.h. es ist kein Online-Shop sondern mehr eine Art Blog mit verschiedenen Geschichten.
Aufgabenstellung
Wichtig ist uns eine schlichtes, minimalistisches Design (vrgl. Tafelwerk) aber trotzdem hochwertig (leicht luxuriös) wirkend.

```html
<!DOCTYPE html>
<html lang="de">
<head>
<meta charset="utf-8">
<title>Lunvo – Neue Geschichten</title>
<link href="https://fonts.googleapis.com/css2?family=Bitter:wght@400;600;700&family=Open+Sans:wght@400;600&display=swap" rel="stylesheet">
<style>
:root{
  --red:#e0211c;
  --ink:#2b2b2b;
  --text:#3c3c3c;
  --card:#edeeed;
  --white:#ffffff;
  --hero-dark:#3a3b3d;
  --hero-mid:#6d7079;
  --hero-skin:#b07c5c;
}
*{margin:0;padding:0;box-sizing:border-box}
html,body{width:1200px;height:2424px;overflow:hidden;background:var(--white);color:var(--ink);font-family:"Open Sans",sans-serif}
a{text-decoration:none;color:inherit}
.site-header{height:116px;display:flex;align-items:center;padding:0 68px;position:relative}
.brand{font-family:"Bitter",serif;font-weight:600;font-size:38px;color:var(--ink);width:184px}
.main-nav{display:flex;gap:34px;font-family:"Bitter",serif;font-size:14px;letter-spacing:.4px}
.main-nav a{color:var(--ink)}
.main-nav a.active{color:var(--red);font-weight:600}
.header-tools{position:absolute;right:78px;top:40px;display:flex;align-items:center;gap:20px}
.header-tools svg{display:block}
.upgrade{font-family:"Bitter",serif;font-weight:600;font-size:15px;color:var(--red);border-bottom:2px solid var(--red);margin-left:30px;margin-right:28px}
.avatar{width:38px;height:38px;border-radius:50%;border:3px solid var(--red);background:radial-gradient(circle at 50% 45%,#9b5a3c,#2a1a14)}
.hero{height:488px;position:relative;background:linear-gradient(100deg,var(--hero-dark) 0%,var(--hero-mid) 40%,var(--hero-skin) 62%,#51402f 78%,#c9c8ca 90%,#e3e2e4 100%)}
.hero h1{position:absolute;left:76px;top:130px;font-family:"Bitter",serif;font-weight:400;font-size:56px;line-height:56px;color:var(--white);letter-spacing:.5px}
.stories{text-align:center}
.stories h2{font-family:"Bitter",serif;font-weight:400;font-size:39px;margin-top:32px;color:var(--ink)}
.filters{display:flex;justify-content:center;gap:56px;margin-top:26px;font-family:"Bitter",serif;font-weight:600;font-size:20px;color:var(--red);padding-left:20px}
.filters span{display:flex;align-items:center;gap:12px}
.card-grid{display:grid;grid-template-columns:340px 340px 340px;column-gap:16px;row-gap:28px;margin:49px 0 0 75px;width:1052px;text-align:left}
.story-card{background:var(--card);height:298px;padding:22px 32px 0 34px}
.story-card .category{font-size:14.5px;color:var(--text)}
.story-card h3{font-family:"Bitter",serif;font-weight:400;font-size:20.5px;line-height:19px;margin-top:12px;color:var(--ink)}
.story-card p{font-size:14.5px;line-height:22.5px;margin-top:14px;color:var(--text)}
.read-more{display:inline-block;margin:18px 0 0 6px;font-family:"Bitter",serif;font-weight:600;font-size:15.5px;color:var(--red);border-bottom:2px solid var(--red);padding:0 3px 1px}
.load-more{display:inline-block;margin-top:68px;font-family:"Bitter",serif;font-weight:600;font-size:20px;color:var(--ink);border-bottom:4px solid var(--red);padding:0 6px 2px}
.site-footer{position:absolute;top:2237px;left:0;width:1200px;border-top:1px solid var(--red);text-align:center}
.footer-nav{display:flex;justify-content:center;gap:34px;margin-top:20px;font-family:"Bitter",serif;font-size:14px;color:var(--ink)}
.footer-brand{font-family:"Bitter",serif;font-weight:600;font-size:52px;margin-top:22px;color:var(--ink)}
.legal{display:flex;justify-content:center;gap:60px;margin-top:18px;font-size:11.5px;font-weight:600;color:#8a8a8a}
.legal a{text-decoration:underline}
</style>
</head>
<body>
<header class="site-header">
  <div class="brand">Lunvo</div>
  <nav class="main-nav">
    <a class="active" href="#">HOME</a><a href="#">KATEGORIEN</a><a href="#">AUTOREN</a><a href="#">ÜBER UNS</a>
  </nav>
  <div class="header-tools">
    <svg width="17" height="17" viewBox="0 0 17 17"><circle cx="7" cy="7" r="5" fill="none" stroke="#e0211c" stroke-width="2.4"/><line x1="10.5" y1="10.5" x2="15" y2="15" stroke="#e0211c" stroke-width="2.6" stroke-linecap="round"/></svg>
    <svg width="13" height="16" viewBox="0 0 13 16"><path d="M1 1h11v14l-5.5-4L1 15z" fill="#e0211c"/></svg>
    <svg width="16" height="17" viewBox="0 0 16 17"><path d="M8 1c3 0 5 2.2 5 5v4l2 3H1l2-3V6c0-2.8 2-5 5-5z" fill="#e0211c"/><circle cx="8" cy="15" r="2" fill="#e0211c"/></svg>
    <a class="upgrade" href="#">Upgrade</a>
    <div class="avatar" role="img" aria-label="Profilbild des Nutzers"></div>
  </div>
</header>

<section class="hero" role="img" aria-label="Foto einer Frau mit lockigem Haar, an einer Wand sitzend">
  <h1>Erotische<br>Kurzgeschichten von<br>Frauen für Frauen</h1>
</section>

<main class="stories">
  <h2>Neue Geschichten bei Lunvo</h2>
  <div class="filters">
    <span>Sortiert nach <svg width="14" height="9" viewBox="0 0 14 9"><path d="M1.5 1.5l5.5 5.5 5.5-5.5" fill="none" stroke="#e0211c" stroke-width="2.6"/></svg></span>
    <span>Kategorie <svg width="14" height="9" viewBox="0 0 14 9"><path d="M1.5 1.5l5.5 5.5 5.5-5.5" fill="none" stroke="#e0211c" stroke-width="2.6"/></svg></span>
    <span>Autor <svg width="14" height="9" viewBox="0 0 14 9"><path d="M1.5 1.5l5.5 5.5 5.5-5.5" fill="none" stroke="#e0211c" stroke-width="2.6"/></svg></span>
  </div>

  <div class="card-grid">
    <article class="story-card"><div class="category">Ferien</div><h3>Nächte in Samt und Seide</h3><p>Lorem ipsum dolor sit amet, consectetuer adipiscing elit. Aenean commodo ligula eget dolor. Aenean massa. Cum sociis natoque penatibus et magnis dis parturient montes, nascetur ridiculus mus.</p><a class="read-more" href="#">Weiterlesen</a></article>
    <article class="story-card"><div class="category">Arbeitsplatz</div><h3>Der Fremde im Zimmer nebenan</h3><p>Lorem ipsum dolor sit amet, consectetuer adipiscing elit. Aenean commodo ligula eget dolor. Aenean massa. Cum sociis natoque penatibus et magnis dis parturient.</p><a class="read-more" href="#">Weiterlesen</a></article>
    <article class="story-card"><div class="category">Alleine</div><h3>Foodporn</h3><p style="margin-top:33px">Lorem ipsum dolor sit amet, consectetuer adipiscing elit. Aenean commodo ligula eget dolor. Aenean massa. Cum sociis natoque penatibus et magnis dis parturient.</p><a class="read-more" href="#">Weiterlesen</a></article>

    <article class="story-card"><div class="category">BDSM</div><h3>Die Flitterwochen</h3><p>Donec pede justo, fringilla vel, aliquet nec, vulputate eget, arcu. In enim justo, rhoncus ut, imperdiet a, venenatis vitae, justo. Nullam dictum felis eu pede mollis pretium.</p><a class="read-more" href="#">Weiterlesen</a></article>
    <article class="story-card"><div class="category">Alleine</div><h3>Spass allein</h3><p>Donec pede justo, fringilla vel, aliquet nec, vulputate eget, arcu. In enim justo, rhoncus ut, imperdiet a, venenatis vitae, justo. Nullam dictum felis eu pede mollis pretium.</p><a class="read-more" href="#">Weiterlesen</a></article>
    <article class="story-card"><div class="category">Lesbisch</div><h3>Die beste Freundin</h3><p>Donec pede justo, fringilla vel, aliquet nec, vulputate eget, arcu. In enim justo, rhoncus ut, imperdiet a, venenatis vitae, justo. Nullam dictum felis eu pede mollis pretium.</p><a class="read-more" href="#">Weiterlesen</a></article>

    <article class="story-card"><div class="category">Ferien</div><h3>Die Urlaubsbekanntschaft</h3><p>Donec pede justo, fringilla vel, aliquet nec, vulputate eget, arcu. In enim justo, rhoncus ut, imperdiet a, venenatis vitae, justo. Nullam dictum felis eu pede mollis pretium.</p><a class="read-more" href="#">Weiterlesen</a></article>
    <article class="story-card"><div class="category">Ferien</div><h3>Quicky am Strand</h3><p>Donec pede justo, fringilla vel, aliquet nec, vulputate eget, arcu. In enim justo, rhoncus ut, imperdiet a, venenatis vitae, justo. Nullam dictum felis eu pede mollis pretium.</p><a class="read-more" href="#">Weiterlesen</a></article>
    <article class="story-card"><div class="category">Schule</div><h3>Die Wette</h3><p>Donec pede justo, fringilla vel, aliquet nec, vulputate eget, arcu. In enim justo, rhoncus ut, imperdiet a, venenatis vitae, justo. Nullam dictum felis eu pede mollis pretium.</p><a class="read-more" href="#">Weiterlesen</a></article>

    <article class="story-card"><div class="category">Dreier</div><h3>Ménage à trois</h3><p>Donec pede justo, fringilla vel, aliquet nec, vulputate eget, arcu. In enim justo, rhoncus ut, imperdiet a, venenatis vitae, justo. Nullam dictum felis eu pede mollis pretium.</p><a class="read-more" href="#">Weiterlesen</a></article>
    <article class="story-card"><div class="category">Ferien</div><h3>Der Fremde in meinem Bett</h3><p>Donec pede justo, fringilla vel, aliquet nec, vulputate eget, arcu. In enim justo, rhoncus ut, imperdiet a, venenatis vitae, justo. Nullam dictum felis eu pede mollis pretium.</p><a class="read-more" href="#">Weiterlesen</a></article>
    <article class="story-card"><div class="category">Sugar / Escort</div><h3>Mit Finanziellem Interesse</h3><p>Donec pede justo, fringilla vel, aliquet nec, vulputate eget, arcu. In enim justo, rhoncus ut, imperdiet a, venenatis vitae, justo. Nullam dictum felis eu pede mollis pretium.</p><a class="read-more" href="#">Weiterlesen</a></article>
  </div>

  <a class="load-more" href="#">Mehr Geschichten laden</a>
</main>

<footer class="site-footer">
  <nav class="footer-nav"><a href="#">HOME</a><a href="#">KATEGORIEN</a><a href="#">AUTOREN</a><a href="#">ÜBER UNS</a></nav>
  <div class="footer-brand">Lunvo</div>
  <div class="legal"><span>© Lunvo GmbH 2021</span><a href="#">Impressum</a><a href="#">AGB</a><a href="#">Datenschutz</a></div>
</footer>
</body>
</html>
```